Business card design for a debt inventory management software company

We need a business card design to help us move into the next phase of our business. We developed an innovative solution to help companies collect their bad debts. We are moving into a new era and branching out into new industries. We are open to design ideas but would like that they have a similar feel/look to our website and include our logo. https://www.ledgorvia.com

Target Market(s)

Finance Industry, Telecom Industry, Utility Industry, Healthcare Industry, Insurance Industry

Industry/Entity Type

Software

Contact Information for Business Card

Include Name, Title, Phone, Email, website, address, and logo

Font styles to use
Sans Serif

Colors

Designer to choose colors to be used in the design.

Requirements
Must have
• A similar look and feel to our website. https://www.ledgorvia.com

```html
<!DOCTYPE html>
<html lang="en">
<head>
<meta charset="utf-8">
<title>Ledgorvia Software – Business Card</title>
<link href="https://fonts.googleapis.com/css2?family=Raleway:wght@400;500;700&display=swap" rel="stylesheet">
<style>
  :root {
    --page-bg: #d8d1c7;
    --card-bg: #f1eee9;
    --card-edge: #ffffff;
    --ink-navy: #3b4777;
    --ink-grey: #6a6864;
    --ink-soft: #7b7873;
  }
  * { margin: 0; padding: 0; box-sizing: border-box; }
  html, body {
    width: 1200px; height: 1047px; overflow: hidden;
    background: var(--page-bg);
    font-family: "Raleway", Arial, sans-serif;
  }
  .business-card {
    position: absolute;
    left: 80px; top: 242px;
    width: 1040px; height: 563px;
    background: var(--card-bg);
    border: 2px solid var(--card-edge);
    box-shadow: 0 10px 30px rgba(60, 50, 40, 0.18);
  }
  .company-name {
    position: absolute; left: 53px; top: 48px;
    font-size: 42px; font-weight: 400; color: var(--ink-navy);
    letter-spacing: 0.2px;
  }
  .company-name .descriptor { color: var(--ink-grey); }
  .person-name {
    position: absolute; left: 55px; top: 174px;
    font-size: 38px; font-weight: 700; color: var(--ink-navy);
    letter-spacing: 2px; text-transform: uppercase;
  }
  .person-title {
    position: absolute; left: 55px; top: 220px;
    font-size: 25px; font-weight: 500; color: var(--ink-soft);
    letter-spacing: 1px;
  }
  .contact-list {
    position: absolute; left: 55px; top: 280px;
    list-style: none;
  }
  .contact-list li {
    display: flex; align-items: center;
    height: 36.5px;
    font-size: 25px; color: var(--ink-grey); letter-spacing: 1px;
  }
  .contact-list svg {
    width: 16px; height: 16px; margin-right: 14px;
    fill: var(--ink-navy);
  }
  .contact-list strong { font-weight: 700; }
  .address {
    position: absolute; left: 53px; top: 448px;
    font-size: 25px; line-height: 36px; color: var(--ink-grey);
    font-style: normal;
  }
  .brand-mark {
    position: absolute; left: 600px; top: 250px;
    width: 380px;
    display: flex; align-items: center; justify-content: center; gap: 16px;
  }
  .brand-mark .brand-square {
    width: 34px; height: 34px; background: var(--ink-navy);
  }
  .brand-mark .brand-word {
    font-size: 54px; font-weight: 700; color: var(--ink-navy);
  }
</style>
</head>
<body>
  <div class="business-card">
    <div class="company-name">Ledgorvia <span class="descriptor">Software</span></div>

    <div class="person-name">Daniel Whitaker</div>
    <div class="person-title">Director</div>

    <ul class="contact-list">
      <li>
        <svg viewBox="0 0 16 16" aria-hidden="true"><path d="M3.2 1.5l2.3-.4 1.4 3.3-1.6 1.2a8 8 0 0 0 4.9 4.9l1.2-1.6 3.3 1.4-.4 2.3c-.2.8-1 1.3-1.8 1.2C6.6 13.3 2.7 9.4 2 3.3c-.1-.8.4-1.6 1.2-1.8z"/></svg>
        555.240.0400
      </li>
      <li>
        <svg viewBox="0 0 16 16" aria-hidden="true"><path d="M4 1h8v4H4zM2 6h12a1 1 0 0 1 1 1v5h-3v3H4v-3H1V7a1 1 0 0 1 1-1zm3 5v3h6v-3z"/></svg>
        555.240.5501
      </li>
      <li>
        <svg viewBox="0 0 16 16" aria-hidden="true"><path d="M1 3h14v10H1zm1.5 1.5v.3L8 8.6l5.5-3.8v-.3zm0 2.1v4.9h11V6.6L8 10.4z"/></svg>
        info@ledgorvia.com
      </li>
      <li>
        <svg viewBox="0 0 16 16" aria-hidden="true"><path d="M8 1a7 7 0 1 0 0 14A7 7 0 0 0 8 1zm-1 1.8V6H3.2A5.5 5.5 0 0 1 7 2.8zm2 0A5.5 5.5 0 0 1 12.8 6H9zM2.6 7.5H7v1H2.6zm6.4 0h4.4v1H9zM3.2 10H7v3.2A5.5 5.5 0 0 1 3.2 10zM9 10h3.8A5.5 5.5 0 0 1 9 13.2z"/></svg>
        www.<strong>ledgorvia</strong>.com
      </li>
    </ul>

    <address class="address">
      48 Harlow Park Avenue,<br>
      Suite 210, Bramfield, Ohio 44390
    </address>

    <div class="brand-mark">
      <span class="brand-square"></span>
      <span class="brand-word">Ledgorvia</span>
    </div>
  </div>
</body>
</html>
```